Happy Birthday Postcard for law firm for existing clients

Need a postcard that will go out to our current clients on their birthdays. Prefer to have our logo incorporated as part of the design so it reminds them about our business. The back needs to say "Happy Birthday from the team at Dunmore Law Firm."

We are a law firm that services local clients. Needs to be mailed so the backside right half needs to be left blank except the return address (in NEEDS below) so it can be mailed with a mailing label.

Target Market(s)

existing customers, varying age range and demographic profile

Industry/Entity Type

Legal

Font styles to use
Sans Serif
Script

Colors

Designer to choose colors to be used in the design.

Requirements
Must have
• Our logo preferrably on the front (can be modified or added to so it fits a birthday message. And needs to be mailed so the back right side needs to be left open for address labels. The firms return address is
• Dunmore Law Firm
• 4718 W Pebblecrest Ave
• Springfield, MO 65917
• Needs to have the text included in the project description on the back, or some close iteration of it if space is limited.
Nice to have
• Some illustration or graphic on the front with the logo that shows it is a birthday postcard

```html
<!DOCTYPE html>
<html lang="en">
<head>
<meta charset="utf-8">
<title>Dunmore Law – Happy Birthday Postcard</title>
<link rel="stylesheet" href="https://fonts.googleapis.com/css2?family=Lato:wght@400&family=Open+Sans:wght@400&family=Pinyon+Script&display=swap">
<style>
  :root {
    --slate-deep: #8a91b6;
    --slate-soft: #b4b9d3;
    --paper: #ffffff;
    --frame-grey: #6d6e72;
    --ink-grey: #5f6064;
    --ink-dark: #333338;
    --script-blue: #4a52b0;
    --script-violet: #3a2c7e;
    --ornament: #5a5fb4;
  }
  * { margin: 0; padding: 0; box-sizing: border-box; }
  html, body { width: 1200px; height: 930px; overflow: hidden; background: var(--paper); }

  .postcard {
    position: relative;
    width: 1200px;
    height: 930px;
    overflow: hidden;
  }

  .harlequin-backdrop {
    position: absolute;
    inset: 0;
    background:
      radial-gradient(ellipse 46% 52% at 50% 50%, rgba(255,255,255,0.85) 0%, rgba(255,255,255,0) 70%),
      linear-gradient(135deg, var(--slate-deep) 0%, var(--slate-soft) 30%, var(--paper) 50%, var(--slate-soft) 70%, var(--slate-deep) 100%);
  }

  .frame-outer {
    position: absolute;
    left: 31px; top: 31px;
    width: 1140px; height: 868px;
    border: 7px solid var(--frame-grey);
  }
  .frame-inner {
    position: absolute;
    left: 44px; top: 44px;
    width: 1112px; height: 842px;
    border: 2px solid var(--frame-grey);
  }

  .corner-flourish {
    position: absolute;
    width: 214px; height: 200px;
    background: linear-gradient(135deg, rgba(90,95,180,0.28), rgba(90,95,180,0) 60%);
  }
  .corner-flourish--tl { left: 72px; top: 72px; }
  .corner-flourish--tr { right: 72px; top: 72px; transform: scaleX(-1); }
  .corner-flourish--bl { left: 72px; bottom: 72px; transform: scaleY(-1); }
  .corner-flourish--br { right: 72px; bottom: 72px; transform: scale(-1, -1); }

  .brand-name {
    position: absolute;
    left: 0; right: 0; top: 243px;
    text-align: center;
    font-family: 'Lato', sans-serif;
    font-weight: 400;
    font-size: 32px;
    letter-spacing: 1px;
    color: var(--ink-grey);
  }

  .brand-rule {
    position: absolute;
    left: 446px; top: 311px;
    width: 308px; height: 1px;
    background: #9a9ba2;
  }

  .greeting-lead {
    position: absolute;
    left: 0; right: 0; top: 322px;
    text-align: center;
    font-family: 'Open Sans', sans-serif;
    font-weight: 400;
    font-size: 46px;
    color: var(--ink-grey);
  }

  .greeting-script {
    position: absolute;
    left: 0; right: 0; top: 372px;
    text-align: center;
    font-family: 'Pinyon Script', cursive;
    font-size: 236px;
    line-height: 1;
    background: linear-gradient(90deg, var(--script-blue), var(--script-violet));
    -webkit-background-clip: text;
    background-clip: text;
    color: transparent;
    filter: drop-shadow(2px 4px 3px rgba(40,40,90,0.18));
  }

  .ribbon-bow {
    position: absolute;
    left: 399px; top: 703px;
    width: 402px; height: 64px;
  }

  .sender-line {
    position: absolute;
    left: 0; right: 0; top: 804px;
    text-align: center;
    font-family: 'Open Sans', sans-serif;
    font-weight: 400;
    font-size: 21px;
    color: var(--ink-dark);
  }
</style>
</head>
<body>
  <main class="postcard">
    <div class="harlequin-backdrop" role="img" aria-label="Harlequin diamond pattern in slate blue, lavender and white"></div>

    <div class="frame-outer"></div>
    <div class="frame-inner"></div>

    <div class="corner-flourish corner-flourish--tl" role="img" aria-label="Celtic knot scroll ornament, top left corner"></div>
    <div class="corner-flourish corner-flourish--tr" role="img" aria-label="Celtic knot scroll ornament, top right corner"></div>
    <div class="corner-flourish corner-flourish--bl" role="img" aria-label="Celtic knot scroll ornament, bottom left corner"></div>
    <div class="corner-flourish corner-flourish--br" role="img" aria-label="Celtic knot scroll ornament, bottom right corner"></div>

    <p class="brand-name">DUNMORE LAW</p>
    <div class="brand-rule"></div>

    <h1 class="greeting-lead">HAPPY</h1>
    <p class="greeting-script">Birthday</p>

    <svg class="ribbon-bow" viewBox="0 0 402 64" role="img" aria-label="Blue ribbon with a bow">
      <defs>
        <linearGradient id="ribbonTone" x1="0" x2="1" y1="0" y2="0">
          <stop offset="0" stop-color="#5a62c0"/>
          <stop offset="1" stop-color="#3a2c7e"/>
        </linearGradient>
      </defs>
      <path d="M0 10 Q200 40 402 24 L402 34 Q200 50 0 20 Z" fill="url(#ribbonTone)" opacity="0.55"/>
    </svg>

    <p class="sender-line">FROM THE TEAM AT DUNMORE LAW FIRM.</p>
  </main>
</body>
</html>
```